A packaging box for a bra that is elegant to display

We are looking for design for our bra box to match our clean and sharp hang tag (see attached). Our color scheme is black/magenta and white. Box should measure 7.5"w x 6"h x 1.25"d. You may incorporate Spot UV coating in your design. We believe less is more and appreciate the clean look with a design that focuses on our logo. This packaging is for a designer product sold in women's boutiques. Attached is my sketch to give you a rough idea of the look we try to achieve. Looking at it now, I would move the logo to the pink section of the box in smaller letters to keep the box clean with a black shiny finish. This is only my first rough idea but I would definitely like to see what comes to your mind.
Updates

I added a eps file with our logo

Colors
e24297
ffffff

Requirements
Nice to have
• I'd like to see samples with angles to show where the item bar code, size etc are going to be on the box.
• Also show your idea of where is opening.

```html
<!DOCTYPE html>
<html lang="en">
<head>
<meta charset="utf-8">
<title>Vellora Bra Box Dieline</title>
<link rel="stylesheet" href="https://fonts.googleapis.com/css2?family=Open+Sans:wght@300;400&display=swap">
<style>
  :root {
    --page: #ffffff;
    --box-black: #000000;
    --lavender-top: #7c81b4;
    --lavender-bottom: #585d8c;
    --ornament: #9196cc;
    --magenta: #e24297;
    --magenta-light: #f17cc0;
    --ink: #25252e;
    --side-text: #b9bde6;
    --dieline: #5fc3dc;
    --label: #ffffff;
  }
  html, body {
    margin: 0;
    padding: 0;
    width: 1200px;
    height: 1200px;
    overflow: hidden;
    background: var(--page);
  }
  .canvas {
    display: block;
    width: 1200px;
    height: 1200px;
  }
  .brand-name {
    font-family: "Open Sans", sans-serif;
    font-weight: 300;
    fill: var(--ink);
  }
  .brand-side {
    font-family: "Open Sans", sans-serif;
    font-weight: 300;
    fill: var(--side-text);
  }
  .tagline {
    font-family: "Open Sans", sans-serif;
    font-weight: 400;
    font-size: 8px;
    letter-spacing: 3px;
    fill: var(--magenta);
  }
  .cut-line {
    fill: none;
    stroke: var(--dieline);
    stroke-width: 1;
  }
  .fold-line {
    fill: none;
    stroke: var(--dieline);
    stroke-width: 0.8;
    stroke-dasharray: 3 3;
  }
  .ornament-area { fill: var(--ornament); }
  .ornament-small { fill: #6a6fa0; }
  .lavender-field { fill: url(#lavenderGradient); }
  .magenta-wave { fill: url(#magentaGradient); }
  .label-panel { fill: var(--label); }
</style>
</head>
<body>
<svg class="canvas" viewBox="0 0 1000 1000" xmlns="http://www.w3.org/2000/svg">
  <defs>
    <linearGradient id="lavenderGradient" x1="0" y1="0" x2="0" y2="1">
      <stop offset="0" stop-color="var(--lavender-top)"/>
      <stop offset="1" stop-color="var(--lavender-bottom)"/>
    </linearGradient>
    <linearGradient id="magentaGradient" x1="0" y1="0" x2="0" y2="1">
      <stop offset="0" stop-color="var(--magenta-light)"/>
      <stop offset="1" stop-color="var(--magenta)"/>
    </linearGradient>
    <clipPath id="dielineShape">
      <path id="outlinePath" d="M8,148 L35,135 L35,52 Q35,40 47,40 L425,40 Q437,40 437,52 L437,130 L440,130 L440,108 L498,112 L505,130 L700,130 A12,12 0 0 0 724,130 L910,130 L913,112 L975,106 L985,112 L985,535 Q985,548 972,548 L513,548 Q500,548 500,535 L500,487 L445,487 L440,463 L8,455 Z"/>
    </clipPath>
  </defs>

  <g class="dieline" clip-path="url(#dielineShape)">
    <rect class="box-base" x="0" y="0" width="1000" height="600" fill="var(--box-black)"/>

    <g class="front-ornament" role="img" aria-label="Lavender lace filigree ornament, front panel">
      <path class="ornament-area" d="M40,350 Q45,190 235,180 Q425,190 430,350 Z"/>
    </g>
    <g class="back-ornament" role="img" aria-label="Lavender lace filigree ornament, back panel">
      <path class="ornament-area" d="M520,350 Q525,190 715,180 Q905,190 910,350 Z"/>
    </g>

    <path class="lavender-field" d="M0,300 Q120,300 230,370 Q360,440 440,285 Q520,440 690,375 Q840,310 1000,295 L1000,600 L0,600 Z"/>
    <path class="magenta-wave" d="M0,282 Q120,280 230,345 Q360,410 440,268 Q520,410 690,352 Q840,290 1000,277 L1000,295 Q840,310 690,375 Q520,440 440,285 Q360,440 230,370 Q120,300 0,300 Z"/>

    <g class="side-ornament" role="img" aria-label="Small lace ornament, left side panel">
      <path class="ornament-small" d="M450,462 Q452,425 472,423 Q492,425 494,462 Z"/>
    </g>
    <g class="side-ornament" role="img" aria-label="Small lace ornament, right side panel">
      <path class="ornament-small" d="M922,460 Q924,425 946,423 Q968,425 970,460 Z"/>
    </g>
  </g>

  <text class="tagline" x="238" y="173" text-anchor="middle">PURE LUXURY</text>
  <text class="tagline" x="712" y="173" text-anchor="middle">PURE LUXURY</text>

  <text class="brand-name" x="58" y="436" font-size="50">VELLORA</text>
  <text class="brand-name" x="886" y="436" font-size="50" text-anchor="end">VELLORA</text>
  <text class="brand-name" x="886" y="504" font-size="30" text-anchor="end">VELLORA</text>

  <text class="brand-side" font-size="26" text-anchor="middle" transform="translate(482,210) rotate(-90)">VELLORA</text>
  <text class="brand-side" font-size="26" text-anchor="middle" transform="translate(956,210) rotate(-90)">VELLORA</text>

  <rect class="label-panel" x="533" y="462" width="80" height="52"/>

  <use href="#outlinePath" class="cut-line"/>
  <g class="folds">
    <line class="fold-line" x1="35" y1="66" x2="437" y2="66"/>
    <line class="fold-line" x1="35" y1="130" x2="437" y2="130"/>
    <line class="fold-line" x1="35" y1="135" x2="35" y2="462"/>
    <line class="fold-line" x1="440" y1="130" x2="440" y2="463"/>
    <line class="fold-line" x1="440" y1="130" x2="505" y2="130"/>
    <line class="fold-line" x1="505" y1="130" x2="505" y2="487"/>
    <line class="fold-line" x1="910" y1="130" x2="910" y2="460"/>
    <line class="fold-line" x1="910" y1="130" x2="985" y2="130"/>
    <line class="fold-line" x1="505" y1="460" x2="985" y2="460"/>
    <line class="fold-line" x1="440" y1="463" x2="505" y2="463"/>
  </g>
</svg>
</body>
</html>
```